PITCH PRESENTATION for Feature Film Project

A while ago I had some key art designed for me for a film project called Cinderpeak's Heir (I see it's still in the online portfolio for inkharborstudio, who did the original work). I'm now taking that project to a series of pitch meetings at a film festival here in Canada and am putting together a powerpoint presentation.
I would want you to use the original design/aesthetic framework across the 14 pages of the presentation. I have provided the text and some image ideas (there's also one video to insert) that you may or may not use, etc. Probably for a large chunk of the pages - perhaps 6 of the ten - you could just clean it up and create a common background theme on which to place the companion text. Obviously, while making it pretty is a priority, it's also a priority for it to be legible to the people whom I'm pitching the project when it is projected onto a large screen.
I've uploaded a draft of the powerpoint text - there could be some minor changes between now and next week. I'll be leaving for the festival on December 3 so, obviously need a final version before that date. I've attached a .jpg of the original artwork along with the powerpoint.

Let me know if you need more details.

I wasn't able to upload the .psd file of the original poster artwork with layers & fonts but here is a link to download it from my dropbox: https://www.boxferrycloud.net/s/k3p8q2rz7tw5xym/GH-Cinderpeak%27s%20Heir%20poster.psd?dl=0 best Derek

This is targeted at some Chinese studio executives to whom the project will be pitched. It is for a film that is a martial arts thriller.

Festival

• The main thing is to use the already-existing material (the poster - incl colour scheme and fonts) as the aesthetic foundation for the presentation. We are, in a sense, trying to strengthen the brand identity of the project with the execs.

```html
<!DOCTYPE html>
<html lang="en">
<head>
<meta charset="utf-8">
<title>Cinderpeak's Heir – Pitch Slide</title>
<link rel="stylesheet" href="https://fonts.googleapis.com/css2?family=Cinzel:wght@400;700&display=swap">
<style>
  :root {
    --gold: #f6b90f;
    --amber: #f5a60a;
    --ink-white: #fbf6ea;
    --rule: rgba(214, 170, 80, 0.75);
    --bg-center: #a67d2c;
    --bg-mid: #7a5419;
    --bg-edge: #2e1b0b;
    --footer-shade: rgba(20, 10, 3, 0.55);
  }
  * { margin: 0; padding: 0; box-sizing: border-box; }
  html, body {
    width: 900px; height: 1200px; overflow: hidden; background: var(--bg-edge);
  }
  .slide {
    position: relative; width: 900px; height: 1200px; overflow: hidden;
    font-family: "Cinzel", "Trajan Pro", serif;
  }
  .slide-texture {
    position: absolute; inset: 0;
    background:
      radial-gradient(ellipse 70% 55% at 55% 38%, var(--bg-center) 0%, var(--bg-mid) 55%, var(--bg-edge) 100%);
  }
  .slide-footer-shade {
    position: absolute; left: 0; right: 0; bottom: 0; height: 200px;
    background: linear-gradient(to bottom, rgba(20,10,3,0) 0%, var(--footer-shade) 60%, rgba(15,8,2,0.8) 100%);
  }
  .slide-title {
    position: absolute; left: 42px; top: 52px;
    font-weight: 400; font-size: 36px; letter-spacing: 1px;
    color: var(--gold); line-height: 1;
  }
  .header-rule, .footer-rule {
    position: absolute; left: 0; width: 900px; height: 2px;
    background: linear-gradient(to right, var(--rule), rgba(214,170,80,0.45));
  }
  .header-rule { top: 112px; }
  .footer-rule { top: 1102px; }
  .still-frame {
    position: absolute; left: 55px; top: 235px; width: 348px; height: 521px;
    border: 6px solid var(--amber);
    background: #efe6d2;
  }
  .still-photo {
    width: 100%; height: 100%;
    background: linear-gradient(160deg, #c9463a 0%, #d9d4c8 30%, #8fc3c9 50%, #a89470 75%, #6b5a3f 100%);
  }
  .still-pointer {
    position: absolute; left: 402px; top: 302px;
  }
  .logline {
    position: absolute; left: 468px; top: 310px; width: 380px;
    color: var(--ink-white); font-weight: 700; font-size: 27px;
    line-height: 45px; letter-spacing: 0.6px;
    text-shadow: 0 1px 2px rgba(0,0,0,0.35);
  }
  .copyright {
    position: absolute; left: 0; width: 900px; top: 1138px;
    text-align: center; color: var(--gold);
    font-weight: 700; font-size: 16px; letter-spacing: 0.4px;
  }
</style>
</head>
<body>
<main class="slide">
  <div class="slide-texture" role="img" aria-label="Aged golden-brown parchment texture with faint swirling ornaments and faded signage"></div>
  <div class="slide-footer-shade"></div>

  <h1 class="slide-title">Cinderpeak's Heir</h1>
  <div class="header-rule"></div>

  <figure class="still-frame">
    <div class="still-photo" role="img" aria-label="Film still: a young woman in a pale blue top and patterned trousers stands holding blades in a ransacked room"></div>
  </figure>
  <svg class="still-pointer" width="20" height="36" viewBox="0 0 20 36" aria-hidden="true">
    <polygon points="0,0 20,18 0,36" fill="var(--amber)"/>
  </svg>

  <p class="logline">A widow's act of vengeance brings the wrath of both the Triad and the police down upon her and her loved ones.</p>

  <div class="footer-rule"></div>
  <p class="copyright">Copyright text here</p>
</main>
</body>
</html>
```